Baufirma sucht Design für Schafkopfkarten
Zielgruppe
Wir sind eine Baufirma und suchen ein schlichtes Design für unsere Schafkopfkarten. Unsere Zielgruppe ist bunt gemischt
Aufgabenstellung
Wir suchen nach einem Design für Schafkopfkarten/Spielkarten.
- Kartenformat 56 x 100 mm
- weißer Rand
- Schlicht
- eventuell Retro Design
- Firmenlogo soll nicht verändert werden
- eventuell 'seit 1946' integrieren

```html
<!DOCTYPE html>
<html lang="de">
<head>
<meta charset="utf-8">
<title>Frielinger Schafkopfkarten – Rückseiten</title>
<link rel="stylesheet" href="https://fonts.googleapis.com/css2?family=Saira:wght@400;700&display=swap">
<style>
  :root {
    --bg: #f3f3f3;
    --card-edge: #ffffff;
    --card-face: #c9c9c9;
    --ink: #4a4d52;
    --ink-soft: #85878a;
    --accent: #f2e33a;
  }
  html, body {
    margin: 0;
    width: 849px;
    height: 1200px;
    overflow: hidden;
    background: var(--bg);
    font-family: "Saira", sans-serif;
  }
  .sheet {
    position: relative;
    width: 849px;
    height: 1200px;
  }
  .card {
    position: absolute;
    top: 399px;
    width: 225px;
    height: 402px;
    background: var(--card-edge);
    border-radius: 22px;
    box-shadow: 0 1px 2px rgba(0,0,0,0.06);
  }
  .card--plain { left: 163px; }
  .card--anniversary { left: 461px; }
  .card__face {
    position: absolute;
    inset: 12px;
    border-radius: 9px;
    background: var(--card-face);
    overflow: hidden;
  }
  .card__pattern {
    position: absolute;
    inset: 0;
    background: linear-gradient(160deg, #cdcdcd, #c3c3c3);
  }
  .brand {
    position: absolute;
    left: 50%;
    width: 200px;
    margin-left: -100px;
    text-align: left;
  }
  .brand--top { top: 78px; transform: rotate(-26deg); }
  .brand--bottom { top: 246px; transform: rotate(154deg); }
  .brand__row {
    display: flex;
    align-items: center;
    gap: 6px;
  }
  .brand__mark {
    width: 18px;
    height: 18px;
    background: var(--accent);
    flex: none;
  }
  .brand__name {
    font-weight: 700;
    font-size: 25px;
    line-height: 1;
    letter-spacing: 0.5px;
    color: var(--ink);
  }
  .brand__tagline {
    margin: 3px 0 0 24px;
    font-size: 8.5px;
    letter-spacing: 0.6px;
    color: var(--ink-soft);
    white-space: nowrap;
  }
  .brand__divider { color: var(--accent); }
  .badge {
    position: absolute;
    left: 50%;
    top: 176px;
    margin-left: -22px;
    padding: 3px 8px;
    background: var(--accent);
    color: var(--ink);
    font-weight: 700;
    font-size: 8.5px;
    letter-spacing: 0.3px;
    transform: rotate(-26deg);
    white-space: nowrap;
  }
</style>
</head>
<body>
<main class="sheet">

  <article class="card card--plain">
    <div class="card__face">
      <div class="card__pattern" role="img" aria-label="Feines graues Würfelmuster als Hintergrund der Kartenrückseite"></div>
      <div class="brand brand--top">
        <div class="brand__row"><span class="brand__mark"></span><span class="brand__name">FRIELINGER</span></div>
        <div class="brand__tagline">TIEFBAU <span class="brand__divider">//</span> ABBRUCH <span class="brand__divider">//</span> RECYCLING</div>
      </div>
      <div class="brand brand--bottom">
        <div class="brand__row"><span class="brand__mark"></span><span class="brand__name">FRIELINGER</span></div>
        <div class="brand__tagline">TIEFBAU <span class="brand__divider">//</span> ABBRUCH <span class="brand__divider">//</span> RECYCLING</div>
      </div>
    </div>
  </article>

  <article class="card card--anniversary">
    <div class="card__face">
      <div class="card__pattern" role="img" aria-label="Feines graues Würfelmuster als Hintergrund der Kartenrückseite"></div>
      <div class="brand brand--top">
        <div class="brand__row"><span class="brand__mark"></span><span class="brand__name">FRIELINGER</span></div>
        <div class="brand__tagline">TIEFBAU <span class="brand__divider">//</span> ABBRUCH <span class="brand__divider">//</span> RECYCLING</div>
      </div>
      <div class="badge">SEIT 1946</div>
      <div class="brand brand--bottom">
        <div class="brand__row"><span class="brand__mark"></span><span class="brand__name">FRIELINGER</span></div>
        <div class="brand__tagline">TIEFBAU <span class="brand__divider">//</span> ABBRUCH <span class="brand__divider">//</span> RECYCLING</div>
      </div>
    </div>
  </article>

</main>
</body>
</html>
```